Up to the Challenge - PPT Template with Splash Slide

We are looking for a PPT template that has 4 slides.
1. Splash slide (Creative, fun, no content, a visual representation of the theme)
2. Section header slide
3. Content Slide
4. Content Slide, another design option
The theme is 'UP to the Challenge'. The design should reflect this theme.
The colors should be in Purple (#864B99), Blue (#0A80C2), and Green (#52B054).

```html
<!DOCTYPE html>
<html lang="en">
<head>
<meta charset="utf-8">
<title>Up to the Challenge – Presentation Template</title>
<link href="https://fonts.googleapis.com/css2?family=Red+Hat+Display:wght@300;400;500;900&display=swap" rel="stylesheet">
<style>
  :root {
    --purple: #864B99;
    --blue: #0A80C2;
    --green: #52B054;
    --ink: #161616;
    --charcoal: #1e1e1e;
    --paper: #ffffff;
    --mist: #f4f4f4;
    --backdrop: #8aa9d4;
  }
  * { box-sizing: border-box; margin: 0; padding: 0; }
  html, body { width: 1200px; height: 737px; overflow: hidden; }
  body {
    background: var(--backdrop);
    font-family: "Red Hat Display", sans-serif;
    position: relative;
    color: var(--ink);
  }
  .slide {
    position: absolute;
    width: 539px;
    height: 303px;
    overflow: hidden;
  }
  .slide--splash { left: 50px; top: 54px; }
  .slide--section { left: 611px; top: 54px; background: var(--charcoal); }
  .slide--content-a { left: 50px; top: 380px; background: var(--paper); }
  .slide--content-b { left: 611px; top: 380px; background: var(--paper); }

  .abs { position: absolute; }

  /* Splash */
  .splash-art {
    position: absolute; inset: 0;
    background:
      radial-gradient(circle at 50% 55%, #5f8a6a 0%, #2f6f72 22%, rgba(20,60,70,0) 45%),
      radial-gradient(circle at 12% 10%, #7b58a6 0%, rgba(123,88,166,0) 40%),
      radial-gradient(circle at 95% 80%, #3fa37a 0%, rgba(63,163,122,0) 45%),
      linear-gradient(135deg, #4d5f9e 0%, #1f6f86 40%, #123c48 70%, #2a8a6a 100%);
  }
  .splash-title {
    position: absolute; left: 12px; top: 24px; width: 539px;
    text-align: center;
    font-weight: 900; font-size: 52px; line-height: 45px;
    color: rgba(160, 200, 220, 0.22);
    letter-spacing: -1px;
  }

  /* Headings */
  .accent-dot { position: absolute; border-radius: 50%; }
  .heading {
    position: absolute;
    font-weight: 900;
    text-transform: uppercase;
    letter-spacing: -0.5px;
  }
  .section-heading { left: 122px; top: 124px; font-size: 35px; line-height: 31px; color: #fff; }
  .section-sub { position: absolute; left: 122px; top: 188px; font-size: 19px; font-weight: 400; color: #fff; }

  .slide-heading { font-size: 30px; line-height: 29px; color: var(--ink); }

  /* Photos */
  .photo { position: absolute; border-radius: 9px; border: 3px solid #fff; box-shadow: 0 2px 8px rgba(0,0,0,0.15); }
  .photo--stage { left: 22px; top: 22px; width: 139px; height: 127px;
    background: linear-gradient(160deg, #4a4a6a 0%, #6b5a5a 45%, #3a3030 100%); }
  .photo--audience { left: 102px; top: 154px; width: 139px; height: 127px;
    background: linear-gradient(170deg, #8a6a45 0%, #4a3e3a 45%, #2a2a33 100%); }
  .photo--meeting { left: 33px; top: 42px; width: 123px; height: 102px; border: none;
    background: linear-gradient(160deg, #3a4a6a 0%, #4a4a55 50%, #2a2a2e 100%); }
  .globe { position: absolute; left: 40px; top: 169px; width: 76px; height: 76px; border-radius: 50%;
    background: radial-gradient(circle at 35% 35%, #8ab8d8 0%, #3c7aa8 45%, #2d5a3e 100%);
    box-shadow: -6px 10px 18px rgba(0,0,0,0.18); }

  .copy-strong { font-weight: 500; }
  .copy-light { font-weight: 300; }

  .content-a-lead { position: absolute; left: 264px; top: 136px; width: 232px; font-size: 10.8px; line-height: 14px; }
  .content-a-body { position: absolute; left: 264px; top: 187px; width: 236px; font-size: 10.8px; line-height: 14px; }

  .card { position: absolute; border-radius: 10px; padding: 10px 9px; }
  .card--note { left: 171px; top: 78px; width: 146px; height: 124px; background: var(--mist);
    box-shadow: 0 2px 6px rgba(0,0,0,0.08); }
  .card--highlight { left: 332px; top: 125px; width: 153px; height: 127px; background: var(--purple); color: #fff; padding: 10px; }
  .card h3 { font-size: 11.5px; line-height: 14px; font-weight: 500; margin-bottom: 1px; }
  .card p { font-size: 10.4px; line-height: 12.8px; font-weight: 300; }

  .intro { position: absolute; left: 342px; top: 25px; width: 150px; }
  .intro h3 { font-size: 11.5px; line-height: 14px; font-weight: 500; margin-bottom: 4px; }
  .intro p { font-size: 11px; line-height: 14px; font-weight: 300; }
</style>
</head>
<body>

  <!-- Splash slide -->
  <section class="slide slide--splash">
    <div class="splash-art" role="img" aria-label="Illustration of children silhouetted before a glowing Earth rising through green and violet mist"></div>
    <div class="splash-title">UP TO THE<br>CHALLENGE</div>
  </section>

  <!-- Section header slide -->
  <section class="slide slide--section">
    <span class="accent-dot" style="left:86px; top:93px; width:72px; height:72px; background:var(--green);"></span>
    <h1 class="heading section-heading">Section<br>Header</h1>
    <p class="section-sub">Lorem Ipsum dolor sit</p>
  </section>

  <!-- Content slide A -->
  <section class="slide slide--content-a">
    <span class="abs" style="left:165px; top:121px; width:32px; height:28px; background:var(--mist); border-radius:5px;"></span>
    <div class="photo photo--stage" role="img" aria-label="Photo of a speaker presenting on stage to a seated audience"></div>
    <div class="photo photo--audience" role="img" aria-label="Photo of a conference audience seen from behind"></div>
    <div class="globe" role="img" aria-label="Rendered globe showing the Americas"></div>

    <span class="accent-dot" style="left:234px; top:48px; width:53px; height:53px; background:var(--purple);"></span>
    <h2 class="heading slide-heading" style="left:261px; top:71px;">Slide<br>Heading</h2>
    <p class="content-a-lead copy-strong">Lorem ipsum dolor sit amet, consectetur adipiscing elit, sed do eiusmod tempor incididunt ut labore et dolore magna aliqua.</p>
    <p class="content-a-body copy-light">Lorem ipsum dolor sit amet, consectetur adipiscing elit, sed do eiusmod tempor incididunt ut labore et dolore magna aliqua. Quis ipsum suspendisse ultrices gravida. Risus commodo viverra maecenas accumsan lacus vel facilisis.</p>
  </section>

  <!-- Content slide B -->
  <section class="slide slide--content-b">
    <span class="abs" style="left:502px; top:9px; width:29px; height:59px; background:var(--green); border-radius:0 14px 0 0;"></span>
    <span class="abs" style="left:502px; top:71px; width:29px; height:28px; background:var(--blue); border-radius:0 14px 0 14px;"></span>
    <div class="photo photo--meeting" role="img" aria-label="Photo of a team discussing around a meeting table"></div>
    <span class="abs" style="left:163px; top:54px; width:23px; height:20px; background:var(--ink); border-radius:4px;"></span>

    <div class="card card--note">
      <h3>Lorem ipsum dolor<br>sit amet,</h3>
      <p>Lorem ipsum dolor sit amet, consectetur adipiscing elit, sed do eiusmod tempor incididunt ut labore et dolore magna aliqua. Quis ipsum suspendisse ultrices gravida.</p>
    </div>

    <div class="intro">
      <h3>Lorem ipsum dolor sit amet,</h3>
      <p>Lorem ipsum dolor sit amet, consectetur adipiscing elit, sed do eiusmod tempor.</p>
    </div>

    <div class="card card--highlight">
      <p>Lorem ipsum dolor sit amet, consectetur adipiscing elit, sed do eiusmod tempor incididunt ut labore et dolore magna aliqua. Quis ipsum suspendisse ultrices gravida. Risus commodo viverra maecenas accumsan lacus vel facilisis.</p>
    </div>

    <span class="accent-dot" style="left:19px; top:197px; width:53px; height:53px; background:var(--blue);"></span>
    <h2 class="heading slide-heading" style="left:46px; top:221px;">Slide<br>Heading</h2>
  </section>

</body>
</html>
```